Business Card Design Project

Require a business card for a swing band called "Velvet Brass Parade". We are a 6 piece band that performs at events and corporate functions. Our music is great for dancing to or just providing a classy background atmosphere for people to enjoy. Final design should communicate professionalism and style with a hint of fun.

Sorry, just realised that it needs to be single sided only. Also, no rounded edges.

Industry/Entity Type

Events

Requirements
Must have
• Contact number: 0438 216 903
email address: velvetbrassparade@mailbox-demo.net
Website details: www.velvetbrassparade-demo.com

```html
<!DOCTYPE html>
<html lang="en">
<head>
<meta charset="utf-8">
<title>Velvet Brass Parade — Business Card</title>
<link rel="stylesheet" href="https://fonts.googleapis.com/css2?family=Source+Sans+3:wght@500&display=swap">
<style>
  :root {
    --card-bg: #a9b8c3;
    --name-brown: #5b4433;
    --ink: #111111;
    --band-light: #9fafba;
    --band-dark: #6e7b85;
  }
  html, body {
    margin: 0;
    padding: 0;
    overflow: hidden;
    background: var(--card-bg);
  }
  .business-card {
    position: relative;
    width: 754px;
    height: 1200px;
    background: var(--card-bg);
    overflow: hidden;
    font-family: "Source Sans 3", sans-serif;
    font-weight: 500;
  }
  .band-name {
    position: absolute;
    left: 120px;
    top: 190px;
    width: 520px;
    margin: 0;
    color: var(--name-brown);
    font-size: 92px;
    line-height: 1.05;
    font-weight: 500;
    letter-spacing: 1px;
  }
  .band-name span { display: block; }
  .band-name .line-2 { padding-left: 110px; }
  .band-name .line-3 { padding-left: 190px; }
  .contact-list {
    position: absolute;
    left: 0;
    right: 0;
    top: 712px;
    margin: 0;
    padding: 0;
    list-style: none;
    text-align: center;
    color: var(--ink);
    font-size: 31px;
    line-height: 49px;
  }
  .music-band {
    position: absolute;
    left: 60px;
    top: 995px;
    width: 650px;
    height: 175px;
    background: linear-gradient(180deg, var(--band-light) 0%, var(--band-dark) 50%, var(--band-light) 100%);
  }
</style>
</head>
<body>
  <main class="business-card">
    <h1 class="band-name">
      <span class="line-1">Velvet</span>
      <span class="line-2">Brass</span>
      <span class="line-3">Parade</span>
    </h1>
    <ul class="contact-list">
      <li class="contact-phone">0438 216 903</li>
      <li class="contact-email">velvetbrassparade@mailbox-demo.net</li>
      <li class="contact-web">www.velvetbrassparade-demo.com</li>
    </ul>
    <div class="music-band" role="img" aria-label="Row of dancing musical note figures along a music staff with a treble clef"></div>
  </main>
</body>
</html>
```